LRW Automotive needs a catchy banner design

We need a design for a banner to be displayed on the fence in the outfield of a baseball stadium to show off our company and have people interested in what we do. We need something catchy that's going to attract people to look over at our banner.
We are a
Complete Automotive Service Company
Tires - Service - Repair - Diesel
We are in a Town called Brookfield Springs
(555)214-3086 we would like the phone number to be a descent size so when you are in the stands you can read it.
I have attached what we came up with but like I said we need it to pop more and make the viewer that's looking at it want to look us up.
The Banner size is 24ft long and 10ft tall

```html
<!DOCTYPE html>
<html lang="en">
<head>
<meta charset="utf-8">
<title>LRW Automotive – Outfield Banner</title>
<link rel="stylesheet" href="https://fonts.googleapis.com/css2?family=Anton&family=Montserrat:wght@400;800;900&family=Oswald:wght@300&display=swap">
<style>
  :root {
    --page-bg: #d6d7d9;
    --panel-dark: #0b111b;
    --panel-mid: #1d2838;
    --blue: #1f7fe6;
    --blue-deep: #0a3f86;
    --blue-light: #3d9cf5;
    --white: #ffffff;
    --ink: #111111;
    --silver-light: #f2f2f2;
    --silver-dark: #7d7f84;
    --rule: #5a6473;
  }
  * { margin: 0; padding: 0; box-sizing: border-box; }
  html, body {
    width: 1126px;
    height: 1200px;
    overflow: hidden;
    background: var(--page-bg);
  }
  .banner {
    position: absolute;
    left: 30px;
    top: 378px;
    width: 1066px;
    height: 444px;
    display: block;
    box-shadow: 0 12px 30px rgba(0,0,0,0.35);
  }
  .brand-name { font-family: "Montserrat", sans-serif; font-weight: 900; fill: var(--blue-light); }
  .tag-lead { font-family: "Anton", sans-serif; fill: var(--white); }
  .headline { font-family: "Anton", sans-serif; }
  .subline { font-family: "Oswald", sans-serif; font-weight: 300; fill: var(--white); }
  .town-line { font-family: "Montserrat", sans-serif; font-weight: 400; fill: var(--white); }
  .town-name { font-weight: 800; fill: var(--blue-light); }
  .phone-number { font-family: "Montserrat", sans-serif; font-weight: 900; fill: var(--ink); }
  .services { font-family: "Montserrat", sans-serif; font-weight: 900; fill: var(--white); }
</style>
</head>
<body>
<svg class="banner" viewBox="0 0 1066 444" xmlns="http://www.w3.org/2000/svg" role="img" aria-label="LRW Automotive banner: We are a Complete Automotive Service Company">
  <defs>
    <linearGradient id="panelFill" x1="0" y1="0" x2="1" y2="1">
      <stop offset="0" stop-color="var(--panel-mid)"/>
      <stop offset="0.55" stop-color="var(--panel-dark)"/>
      <stop offset="1" stop-color="#151d2a"/>
    </linearGradient>
    <linearGradient id="chrome" x1="0" y1="0" x2="0" y2="1">
      <stop offset="0" stop-color="var(--silver-dark)"/>
      <stop offset="0.45" stop-color="var(--silver-light)"/>
      <stop offset="0.55" stop-color="#9a9ca1"/>
      <stop offset="1" stop-color="var(--silver-light)"/>
    </linearGradient>
    <linearGradient id="blueMetal" x1="0" y1="0" x2="0" y2="1">
      <stop offset="0" stop-color="var(--blue-deep)"/>
      <stop offset="0.45" stop-color="var(--blue-light)"/>
      <stop offset="0.55" stop-color="var(--blue)"/>
      <stop offset="1" stop-color="var(--blue-light)"/>
    </linearGradient>
    <linearGradient id="bandFill" x1="0" y1="0" x2="1" y2="0">
      <stop offset="0" stop-color="var(--blue)"/>
      <stop offset="1" stop-color="var(--blue-deep)"/>
    </linearGradient>
  </defs>

  <rect class="panel" width="1066" height="444" fill="url(#panelFill)"/>

  <!-- brand lockup -->
  <g class="brand">
    <rect x="52" y="160" width="26" height="26" fill="var(--blue-light)"/>
    <text class="brand-name" x="92" y="186" font-size="34">LRW Automotive</text>
  </g>

  <!-- headline block -->
  <g class="headline-block">
    <polygon class="tag-band" points="520,52 676,52 703,98 520,98" fill="url(#bandFill)"/>
    <text class="tag-lead" x="534" y="90" font-size="34" transform="skewX(-10)" transform-origin="534 90">WE ARE A</text>
    <line x1="703" y1="98.5" x2="1022" y2="98.5" stroke="var(--rule)" stroke-width="1"/>
    <text class="headline" x="516" y="179" font-size="84" fill="url(#chrome)" stroke="#3a3d44" stroke-width="1"
          textLength="316" lengthAdjust="spacingAndGlyphs" transform="skewX(-10)" transform-origin="516 179">COMPLETE</text>
    <text class="headline" x="590" y="258" font-size="84" fill="url(#blueMetal)" stroke="#3a3d44" stroke-width="1"
          textLength="396" lengthAdjust="spacingAndGlyphs" transform="skewX(-10)" transform-origin="590 258">AUTOMOTIVE</text>
    <text class="subline" x="590" y="311" font-size="44" textLength="378" lengthAdjust="spacing">SERVICE COMPANY</text>
    <line x1="530" y1="338.5" x2="1028" y2="338.5" stroke="var(--rule)" stroke-width="1"/>
  </g>

  <!-- location -->
  <text class="town-line" x="29" y="341" font-size="22">We are in a Town called <tspan class="town-name">Brookfield Springs</tspan></text>

  <!-- phone bar -->
  <g class="phone-bar">
    <polygon points="29,355 456,355 485,410 29,410" fill="var(--white)"/>
    <polygon points="29,355 90,355 120,410 58,410" fill="var(--blue)"/>
    <g class="phone-icon" transform="translate(66,382)" fill="var(--white)">
      <path d="M-9,-9 c2,-2 4,-2 5,0 l2,4 c1,2 0,3 -1,4 l-1,1 c1,3 3,5 6,6 l1,-1 c1,-1 2,-2 4,-1 l4,2 c2,1 2,3 0,5 l-2,2 c-3,2 -10,-1 -15,-6 s-8,-12 -6,-15 z"/>
      <path d="M2,-11 a12,12 0 0 1 10,10" fill="none" stroke="var(--white)" stroke-width="2"/>
      <path d="M2,-6 a7,7 0 0 1 5,5" fill="none" stroke="var(--white)" stroke-width="2"/>
    </g>
    <text class="phone-number" x="160" y="396" font-size="34" textLength="285" lengthAdjust="spacingAndGlyphs">(555)214-3086</text>
  </g>

  <!-- services band -->
  <g class="services-bar">
    <polygon points="468,355 1006,355 1036,410 498,410" fill="url(#bandFill)"/>
    <text class="services" x="515" y="393" font-size="25" textLength="470" lengthAdjust="spacingAndGlyphs">TIRES - SERVICE - REPAIR - DIESEL</text>
  </g>
</svg>
</body>
</html>
```